Chatterwall and Glimmerly advertising

We need Chatterwall and Glimmerly ads. Simple ad with Alaska themed background.
This ad is to introduce our new KESTREL Internet service.
--Speeds to 500 mpbs
-- Packages start at only $89.99 for speeds to 100mbps
-- Fiber Optic based connection, Not satellite
-- Extreme low latency, consistent speeds
--FREE equipment, FREE Installation, FREE wifi router, First month of service FREE

```html
<!DOCTYPE html>
<html lang="en">
<head>
<meta charset="utf-8">
<title>KESTREL Internet service – ad set</title>
<link rel="stylesheet" href="https://fonts.googleapis.com/css2?family=Fira+Sans+Condensed:ital,wght@0,300;0,500;0,600;0,700;1,300;1,600;1,700&family=Fira+Sans:wght@600;700&display=swap">
<style>
  :root {
    --page: #ffffff;
    --night: #000000;
    --sky-deep: #0b1f3a;
    --sky-mid: #1d4b78;
    --tile: #12559f;
    --tile-light: #7fc2ee;
    --white: #ffffff;
    --red: #e3212f;
    --free-blue: #1e73be;
  }
  * { margin: 0; padding: 0; box-sizing: border-box; }
  html, body { width: 1200px; height: 1199px; overflow: hidden; background: var(--page); }
  body { position: relative; font-family: "Fira Sans Condensed", sans-serif; color: var(--white); }

  .ad { position: absolute; background: var(--night); overflow: hidden; }
  .ad--tall { left: 65px; top: 65px; width: 528px; height: 674px; }
  .ad--square { left: 626px; top: 145px; width: 530px; height: 530px; }
  .ad--wide { left: 261px; top: 779px; width: 719px; height: 378px; }

  .night-sky {
    position: absolute; left: 0; top: 0; width: 100%;
    background:
      radial-gradient(circle at 82% 72%, rgba(230,245,255,.9) 0, rgba(120,180,230,.45) 6%, transparent 18%),
      linear-gradient(160deg, transparent 20%, rgba(140,190,230,.35) 38%, transparent 55%),
      linear-gradient(180deg, var(--sky-deep) 0%, var(--sky-mid) 60%, #0a1a2e 85%, var(--night) 100%);
  }
  .ad--tall .night-sky { height: 300px; }
  .ad--square .night-sky { height: 190px; }
  .ad--wide .night-sky { height: 160px; background:
      radial-gradient(circle at 80% 52%, rgba(230,245,255,.9) 0, rgba(120,180,230,.45) 6%, transparent 18%),
      linear-gradient(165deg, transparent 25%, rgba(140,190,230,.35) 42%, transparent 58%),
      linear-gradient(180deg, var(--sky-deep) 0%, var(--sky-mid) 60%, #0a1a2e 85%, var(--night) 100%); }

  .headline { position: absolute; font-family: "Fira Sans", sans-serif; font-weight: 700; line-height: 1; white-space: nowrap; text-shadow: 0 2px 6px rgba(0,0,0,.5); }
  .tagline { font-family: "Fira Sans Condensed", sans-serif; font-style: italic; font-weight: 300; letter-spacing: -0.5px; text-shadow: 0 2px 6px rgba(0,0,0,.5); }

  .ad--tall .headline { left: 0; width: 100%; top: 92px; text-align: center; font-size: 100px; }
  .ad--tall .tagline { position: absolute; left: 0; width: 100%; text-align: center; top: 196px; font-size: 52px; line-height: 1; }

  .ad--square .headline { left: 0; width: 100%; top: 62px; text-align: center; font-size: 58px; }
  .ad--square .headline .tagline { font-size: 34px; margin-left: 8px; }

  .ad--wide .headline { left: 44px; top: 58px; font-size: 64px; }
  .ad--wide .headline .tagline { font-size: 40px; margin-left: 10px; }

  .speeds { position: absolute; color: var(--red); font-style: italic; font-weight: 600; line-height: 1; white-space: nowrap; }
  .ad--tall .speeds { left: 0; width: 100%; text-align: center; top: 302px; font-size: 40px; }
  .ad--square .speeds { left: 0; width: 100%; text-align: center; top: 190px; font-size: 40px; }
  .ad--wide .speeds { left: 48px; top: 138px; font-size: 38px; }

  .features { position: absolute; display: flex; gap: 12px; }
  .feature { background: var(--tile); border-radius: 6px; display: flex; flex-direction: column; justify-content: center; align-items: center; text-align: center; color: var(--tile-light); font-weight: 300; line-height: 1.2; }
  .feature strong { color: var(--white); font-weight: 500; }
  .feature .price { color: var(--white); font-weight: 700; line-height: 1.05; }
  .feature .fine { color: var(--tile-light); font-style: italic; font-weight: 600; }

  .ad--tall .features { left: 68px; top: 357px; }
  .ad--tall .feature, .ad--square .feature { width: 122px; height: 132px; font-size: 19px; }
  .ad--square .features { left: 70px; top: 243px; }
  .ad--tall .price, .ad--square .price { font-size: 32px; }
  .ad--tall .fine, .ad--square .fine { font-size: 11px; }

  .ad--wide .features { left: 180px; top: 189px; gap: 10px; }
  .ad--wide .feature { width: 112px; height: 107px; font-size: 16px; }
  .ad--wide .price { font-size: 28px; }
  .ad--wide .fine { font-size: 10px; }

  .free-offer { position: absolute; border: 1.5px solid var(--red); border-radius: 8px; display: flex; align-items: center; }
  .free-offer .free { color: var(--free-blue); font-weight: 600; line-height: 1; }
  .free-offer .items { color: var(--white); font-weight: 500; line-height: 1.5; }
  .ad--tall .free-offer { left: 68px; top: 500px; width: 390px; height: 61px; padding-left: 11px; }
  .ad--square .free-offer { left: 70px; top: 386px; width: 389px; height: 61px; padding-left: 11px; }
  .ad--tall .free, .ad--square .free { font-size: 54px; width: 126px; }
  .ad--tall .items, .ad--square .items { font-size: 16.5px; }
  .ad--wide .free-offer { left: 48px; top: 312px; width: 619px; height: 43px; padding-left: 8px; }
  .ad--wide .free { font-size: 40px; width: 96px; }
  .ad--wide .items { font-size: 20px; }

  .brand { position: absolute; font-weight: 600; font-size: 18px; color: var(--white); white-space: nowrap; line-height: 1; }
  .ad--tall .brand { left: 0; width: 100%; text-align: center; top: 628px; }
  .ad--square .brand { left: 0; width: 100%; text-align: center; top: 490px; }
  .ad--wide .brand { left: 550px; top: 280px; }
</style>
</head>
<body>

<section class="ad ad--tall" aria-label="KESTREL Internet service ad, tall">
  <div class="night-sky" role="img" aria-label="Starry Alaskan night sky with a glowing light over dark mountain silhouettes"></div>
  <h1 class="headline">KESTREL</h1>
  <p class="tagline">Internet service.</p>
  <p class="speeds">Speeds to 500 mpbs</p>
  <div class="features">
    <div class="feature">Packages<br>start at only<span class="price">$89.99</span><span class="fine">for speeds to 100mbps</span></div>
    <div class="feature"><strong>Fiber Optic</strong>based<br>connection,<br>Not satellite</div>
    <div class="feature">Extreme<br>low latency,<strong>consistent<br>speeds</strong></div>
  </div>
  <div class="free-offer"><span class="free">FREE</span><span class="items">Equipment, Installation,<br>Wifi Router &amp; First Month of Service</span></div>
  <p class="brand">Aurora Ridge</p>
</section>

<section class="ad ad--square" aria-label="KESTREL Internet service ad, square">
  <div class="night-sky" role="img" aria-label="Starry Alaskan night sky with a glowing light over dark mountain silhouettes"></div>
  <h1 class="headline">KESTREL<span class="tagline">Internet service.</span></h1>
  <p class="speeds">Speeds to 500 mpbs</p>
  <div class="features">
    <div class="feature">Packages<br>start at only<span class="price">$89.99</span><span class="fine">for speeds to 100mbps</span></div>
    <div class="feature"><strong>Fiber Optic</strong>based<br>connection,<br>Not satellite</div>
    <div class="feature">Extreme<br>low latency,<strong>consistent<br>speeds</strong></div>
  </div>
  <div class="free-offer"><span class="free">FREE</span><span class="items">Equipment, Installation,<br>Wifi Router &amp; First Month of Service</span></div>
  <p class="brand">Aurora Ridge</p>
</section>

<section class="ad ad--wide" aria-label="KESTREL Internet service ad, wide">
  <div class="night-sky" role="img" aria-label="Starry Alaskan night sky with a glowing light over dark mountain silhouettes"></div>
  <h1 class="headline">KESTREL<span class="tagline">Internet service.</span></h1>
  <p class="speeds">Speeds to 500 mpbs</p>
  <div class="features">
    <div class="feature">Packages<br>start at only<span class="price">$89.99</span><span class="fine">for speeds to 100mbps</span></div>
    <div class="feature"><strong>Fiber Optic</strong>based<br>connection,<br>Not satellite</div>
    <div class="feature">Extreme<br>low latency,<strong>consistent<br>speeds</strong></div>
  </div>
  <p class="brand">Aurora Ridge</p>
  <div class="free-offer"><span class="free">FREE</span><span class="items">Equipment, Installation, Wifi Router &amp; First Month of Service</span></div>
</section>

</body>
</html>
```